Business Card for Orthopaedic Clinic.
Should have nice design, double sided that includes logo
Should include my name, my contact, my email, webpage. A QR code to scan business card.

please use dummy information for privacy reasons. I will provide my name, email, practice address once a winner is selected.

Target Market(s)

Future patients

Contact Information for Business Card

Name: Dr Rao
Contact No: +65 90417362
Practice Address: Singapore
Email: doctor@velmor.com
Website: www.velmor.com

Colors
00a990

Requirements
Must have
• Logo and a nice colour scheme.
A QR Code for Contact Card.
Name
Contact
Practice Address
Email
Website.
Nice to have
• Nice colour scheme
Should not have
• Nothing too cluttered.

```html
<!DOCTYPE html>
<html lang="en">
<head>
<meta charset="utf-8">
<title>Velmor Orthopaedics Stationery</title>
<link href="https://fonts.googleapis.com/css2?family=Arimo:wght@400;700&family=Montserrat:wght@400;500;700&display=swap" rel="stylesheet">
<style>
  :root {
    --teal: #4fb1ad;
    --slate: #5a646e;
    --ink: #3e4348;
    --paper: #f5f5f5;
    --backdrop: #e3e3e3;
  }
  * { box-sizing: border-box; margin: 0; padding: 0; }
  html, body { width: 1200px; height: 1200px; overflow: hidden; }
  body { background: var(--backdrop); position: relative; font-family: "Arimo", Arial, sans-serif; color: var(--ink); }

  .brand { position: absolute; display: flex; align-items: center; gap: 6px; font-family: "Montserrat", Arial, sans-serif; font-weight: 500; color: var(--slate); }
  .brand-square { background: var(--teal); flex: none; }
  .brand-name { line-height: 1.05; letter-spacing: 0.08em; }

  /* Letterhead */
  .letterhead { position: absolute; left: 132px; top: 161px; width: 621px; height: 878px; background: var(--paper); overflow: hidden; }
  .letterhead .brand { left: 54px; top: 61px; gap: 9px; }
  .letterhead .brand-square { width: 40px; height: 42px; }
  .letterhead .brand-name { font-size: 15px; }
  .letterhead .brand-name span { display: block; font-size: 11px; font-weight: 400; letter-spacing: 0.3em; }
  .letter-block { position: absolute; left: 54px; width: 513px; font-size: 9px; line-height: 12.6px; }
  .letter-block p { text-align: justify; }
  .date { top: 193px; }
  .recipient { top: 218px; }
  .salutation { top: 306px; font-weight: 700; }
  .para-1 { top: 343px; }
  .para-2 { top: 394px; }
  .para-3 { top: 456px; }
  .para-4 { top: 531px; }
  .closing { top: 620px; }
  .signature { position: absolute; left: 54px; top: 654px; width: 66px; height: 16px; background: #dcdfe0; }
  .signer { top: 682px; }
  .letter-footer { position: absolute; left: 54px; top: 834px; display: flex; gap: 20px; font-family: "Montserrat", Arial, sans-serif; font-size: 10px; color: var(--slate); }
  .letter-footer span, .card-contacts li { display: flex; align-items: center; gap: 3px; }
  .bottom-bar { position: absolute; left: 0; bottom: 0; width: 100%; height: 15px; }

  /* Cards */
  .card { position: absolute; left: 804px; width: 263px; overflow: hidden; }
  .card-front { top: 223px; height: 150px; background: var(--teal); }
  .card-front .brand { left: 23px; top: 101px; color: #fff; }
  .card-front .brand-square { width: 27px; height: 27px; background: #fff; }
  .card-front .brand-name { font-size: 11px; }
  .card-front .brand-name span { display: block; font-size: 7.5px; font-weight: 400; letter-spacing: 0.3em; }

  .card-back { top: 429px; height: 151px; background: var(--paper); }
  .card-back .brand { left: 19px; top: 19px; gap: 4px; }
  .card-back .brand-square { width: 20px; height: 20px; }
  .card-back .brand-name { font-size: 8.5px; }
  .card-back .brand-name span { display: block; font-size: 5.5px; font-weight: 400; letter-spacing: 0.3em; }
  .card-name { position: absolute; right: 19px; top: 75px; font-weight: 700; font-size: 10px; color: var(--teal); }
  .card-rule { position: absolute; left: 19px; top: 90px; width: 225px; height: 1px; background: var(--slate); }
  .card-contacts { position: absolute; left: 19px; top: 99px; list-style: none; font-family: "Montserrat", Arial, sans-serif; font-size: 6.5px; line-height: 9px; color: var(--slate); }
  .card-back .bottom-bar { height: 8px; }
</style>
</head>
<body>

<section class="letterhead">
  <div class="brand">
    <div class="brand-square"></div>
    <div class="brand-name">VELMOR<span>ORTHOPAEDICS</span></div>
  </div>

  <p class="letter-block date">December 25, 2020</p>
  <p class="letter-block recipient">Mr. John Doe<br>President<br>AA Corporation<br>111 Street Name, Suite#<br>City, State, 12345</p>
  <p class="letter-block salutation">Dear Mr. John,</p>
  <div class="letter-block para-1"><p>Lorem ipsum dolor sit amet, consectetur adipiscing elit. Integer diam quam, egestas eu ultrices eu, suscipit ac sapien. Phasellus eu dui nisi. Nam et euismod diam, nec lobortis tortor. Donec et diam nulla. Aenean varius tincidunt convallis. Aliquam a tortor at lacus dictum aliquet. Nunc laoreet metus sapien, in scelerisque augue consectetur in.</p></div>
  <div class="letter-block para-2"><p>Fusce nec justo laoreet, egestas justo sed, aliquet sem. Pellentesque pharetra massa non orci bibendum semper. Pellentesque cursus eu lectus a consectetur. Nunc volutpat suscipit posuere. Vestibulum facilisis vel quam malesuada mattis. Nulla in mattis tellus. Maecenas tristique mauris vitae pharetra tincidunt. In ut ornare risus. Integer molestie vestibulum nisi, semper dapibus mi condimentum eu.</p></div>
  <div class="letter-block para-3"><p>Nullam sagittis elit libero, id fringilla est tincidunt eget. Donec in ipsum ultricies, consectetur quam vel, facilisis elit. Phasellus tincidunt congue risus vel luctus. Suspendisse ut mollis neque. Donec ornare orci in turpis vestibulum, in ultrices metus scelerisque. Pellentesque mattis mattis nunc, nec tincidunt lacus egestas id. Fusce facilisis sagittis neque sit amet vulputate. Aliquam ut eros lobortis tortor facilisis vehicula. Sed sed luctus leo, at laoreet sapien. Donec placerat adipiscing ligula non euismod. In lobortis pretium nisl id luctus.</p></div>
  <div class="letter-block para-4"><p>Integer gravida tincidunt nibh, scelerisque tincidunt turpis. Suspendisse potenti. Nunc hendrerit euismod lectus id elementum. Fusce vitae gravida velit, quis eleifend lectus. In imperdiet mauris eu dui viverra sagittis. Donec tempor dui diam, condimentum gravida lacus pretium a. Nullam fringilla augue quis arcu placerat scelerisque. Aliquam nec tincidunt augue, sit amet posuere ipsum.</p></div>
  <p class="letter-block closing">Sincerely Yours,</p>
  <div class="signature" role="img" aria-label="Handwritten signature of Dr. Rao"></div>
  <p class="letter-block signer">Dr. Rao<br>President</p>

  <div class="letter-footer">
    <span><svg width="9" height="9" viewBox="0 0 10 10"><path d="M2 0.5l2 2-1 1.2c.6 1.3 1.6 2.3 2.9 2.9l1.2-1 2 2-1.2 1.6C4.6 9 1 5.4.4 1.7z" fill="var(--teal)"/></svg>+65 90417362</span>
    <span><svg width="9" height="7" viewBox="0 0 10 8"><rect x=".5" y=".5" width="9" height="7" fill="none" stroke="var(--teal)"/><path d="M.5.5L5 4.5 9.5.5" fill="none" stroke="var(--teal)"/></svg>doctor@velmor.com</span>
    <span><svg width="9" height="9" viewBox="0 0 10 10"><circle cx="5" cy="5" r="4.5" fill="none" stroke="var(--teal)"/><ellipse cx="5" cy="5" rx="2" ry="4.5" fill="none" stroke="var(--teal)"/><path d="M.5 5h9" stroke="var(--teal)"/></svg>www.velmor.com</span>
    <span><svg width="7" height="10" viewBox="0 0 7 10"><path d="M3.5 0A3.5 3.5 0 0 0 0 3.5C0 6 3.5 10 3.5 10S7 6 7 3.5A3.5 3.5 0 0 0 3.5 0zm0 5a1.5 1.5 0 1 1 0-3 1.5 1.5 0 0 1 0 3z" fill="var(--teal)"/></svg>SINGAPORE</span>
  </div>

  <svg class="bottom-bar" viewBox="0 0 621 15" preserveAspectRatio="none">
    <rect width="621" height="15" fill="var(--slate)"/>
    <polygon points="0,0 436,0 420,15 0,15" fill="var(--teal)"/>
  </svg>
</section>

<section class="card card-front">
  <div class="brand">
    <div class="brand-square"></div>
    <div class="brand-name">VELMOR<span>ORTHOPAEDICS</span></div>
  </div>
</section>

<section class="card card-back">
  <div class="brand">
    <div class="brand-square"></div>
    <div class="brand-name">VELMOR<span>ORTHOPAEDICS</span></div>
  </div>
  <p class="card-name">Dr RAO</p>
  <div class="card-rule"></div>
  <ul class="card-contacts">
    <li><svg width="6" height="6" viewBox="0 0 10 10"><path d="M2 0.5l2 2-1 1.2c.6 1.3 1.6 2.3 2.9 2.9l1.2-1 2 2-1.2 1.6C4.6 9 1 5.4.4 1.7z" fill="var(--teal)"/></svg>+65 90417362</li>
    <li><svg width="6" height="5" viewBox="0 0 10 8"><rect x=".5" y=".5" width="9" height="7" fill="none" stroke="var(--teal)"/><path d="M.5.5L5 4.5 9.5.5" fill="none" stroke="var(--teal)"/></svg>doctor@velmor.com</li>
    <li><svg width="6" height="6" viewBox="0 0 10 10"><circle cx="5" cy="5" r="4.5" fill="none" stroke="var(--teal)"/><path d="M.5 5h9" stroke="var(--teal)"/></svg>www.velmor.com</li>
    <li><svg width="5" height="6" viewBox="0 0 7 10"><path d="M3.5 0A3.5 3.5 0 0 0 0 3.5C0 6 3.5 10 3.5 10S7 6 7 3.5A3.5 3.5 0 0 0 3.5 0z" fill="var(--teal)"/></svg>SINGAPORE</li>
  </ul>
  <svg class="bottom-bar" viewBox="0 0 263 8" preserveAspectRatio="none">
    <rect width="263" height="8" fill="var(--slate)"/>
    <polygon points="0,0 171,0 164,8 0,8" fill="var(--teal)"/>
  </svg>
</section>

</body>
</html>
```